Medical Skincare services/menu/pricing Booklet 12 pages

We need produce a 12-page glossy, saddle-stitched booklet (5 1/2" tall X 81/2" wide). The booklet will be used as a services menu for a skin care salon. I have mocked up the booklet (w/ all copy) in WORD and I've provided a separate PDF of the accurate page order (see files attached). IMPORTANT: Feel free to use your creativity yet style-wise it should kinda match my wife's website colors and text style. Her clients are demanding so she wants a clean, high end, modern look (ala Pebble maybe?). See her website for a frame of reference www.GlowWithMarta.com

Target Market(s)

upscale female, professional women, teens with acne

Industry/Entity Type

Medical

Requirements
Must have
• the pics in the mock up are important. I've attached them here

```html
<!DOCTYPE html>
<html lang="en">
<head>
<meta charset="utf-8">
<title>Glow With Marta – Services Booklet Cover</title>
<link href="https://fonts.googleapis.com/css2?family=Oswald:wght@600&family=Exo+2:wght@300;600&display=swap" rel="stylesheet">
<style>
  :root {
    --backdrop: #a3a3a3;
    --cover-black: #050505;
    --silver: #d9d9d9;
    --silver-soft: #bdbdbd;
    --rule-dark: #1e1e1e;
  }
  html, body {
    margin: 0;
    padding: 0;
    width: 1200px;
    height: 900px;
    overflow: hidden;
    background: var(--backdrop);
  }
  .booklet-cover {
    position: absolute;
    left: 40px;
    top: 88px;
    width: 1120px;
    height: 724px;
    background: var(--cover-black);
    overflow: hidden;
  }
  .brand-name {
    position: absolute;
    left: 0;
    right: 0;
    top: 200px;
    margin: 0;
    text-align: center;
    font-family: "Oswald", "Arial Narrow", sans-serif;
    font-weight: 600;
    font-size: 112px;
    line-height: 1;
    letter-spacing: 4px;
    text-transform: uppercase;
    color: var(--silver);
  }
  .site-address {
    position: absolute;
    left: 300px;
    top: 500px;
    margin: 0;
    font-family: "Exo 2", sans-serif;
    font-weight: 300;
    font-size: 30px;
    color: var(--silver);
    letter-spacing: 0.5px;
  }
  .site-address .site-name {
    font-weight: 600;
  }
  .site-rule {
    position: absolute;
    left: 300px;
    top: 552px;
    width: 330px;
    height: 3px;
    background: linear-gradient(90deg, var(--silver-soft), var(--silver));
  }
  .base-rule {
    position: absolute;
    left: 0;
    top: 640px;
    width: 640px;
    height: 4px;
    background: linear-gradient(90deg, var(--rule-dark) 0%, var(--silver-soft) 55%, var(--rule-dark) 100%);
  }
</style>
</head>
<body>
  <main class="booklet-cover">
    <h1 class="brand-name">Glow With Marta</h1>
    <p class="site-address">www.<span class="site-name">GlowWithMarta</span>.com</p>
    <div class="site-rule"></div>
    <div class="base-rule"></div>
  </main>
</body>
</html>
```